Business Card Design

This is a new business to be run from my home. I have attended certificate workshops run by Dr Derek Onwu who is a Master Trainer in Harbor Steps Method.
I wish to communicate to people that Tai Chi is for everyone, no matter their age, gender or fitness levels. Tai Chi is taught both standing & seated.
The card should have a slightly Asian feel, mainly printed in black & white with perhaps a little soft pink &/or green.

Target Market(s)

people of all ages from 10 years up, poor fitness & mild disabilities.

Industry/Entity Type

Fitness

Contact Information for Business Card

Wexmoor Tai Chi for Fitness, Health & Relaxation

Branna Holt, Certificated Leader

ph 4091 5528

Requirements
Nice to have
• a feeling of health & peace.
Should not have
• bright colours, fancy fonts

```html
<!DOCTYPE html>
<html lang="en">
<head>
<meta charset="utf-8">
<title>Wexmoor Tai Chi for Fitness – Business Card</title>
<link rel="stylesheet" href="https://fonts.googleapis.com/css2?family=Open+Sans:wght@400;700&display=swap">
<style>
  :root {
    --page: #ffffff;
    --field-top: #7fa48d;
    --field-mid: #6d967d;
    --field-low: #577e67;
    --field-deep: #4a6e59;
    --band-top: #c48c9c;
    --band-bottom: #d9a5b3;
    --title-ink: #ffffff;
    --title-shade: rgba(20, 30, 25, 0.55);
    --text-light: #f7f7f5;
    --text-accent: #f3e3b4;
    --phone-ink: #2b2b2b;
    --figure-tone: #eef0ee;
    --ornament-tone: rgba(235, 242, 236, 0.22);
  }
  * { margin: 0; padding: 0; box-sizing: border-box; }
  html, body {
    width: 1200px;
    height: 741px;
    overflow: hidden;
    background: var(--page);
  }
  .canvas {
    position: relative;
    width: 1200px;
    height: 741px;
    background: var(--page);
  }
  .card {
    position: absolute;
    left: 45px;
    top: 45px;
    width: 1110px;
    height: 649px;
    overflow: hidden;
  }
  .card__field {
    position: absolute;
    left: 0;
    top: 0;
    width: 100%;
    height: 548px;
    background: linear-gradient(180deg, var(--field-top) 0%, var(--field-mid) 45%, var(--field-low) 85%, var(--field-deep) 100%);
  }
  .card__band {
    position: absolute;
    left: 0;
    top: 548px;
    width: 100%;
    height: 101px;
    background: linear-gradient(180deg, var(--band-top), var(--band-bottom));
  }
  .card__title {
    position: absolute;
    left: 0;
    right: 0;
    top: 40px;
    text-align: center;
    font-family: "Open Sans", "Helvetica Neue", Arial, sans-serif;
    font-weight: 700;
    font-size: 52px;
    line-height: 1.2;
    letter-spacing: 2px;
    color: var(--title-ink);
    text-shadow: 2px 3px 4px var(--title-shade);
    white-space: nowrap;
  }
  .card__ornament {
    position: absolute;
    left: 95px;
    top: 40px;
    width: 300px;
    height: 500px;
    border-radius: 40% 60% 50% 50%;
    background: radial-gradient(ellipse at 60% 40%, var(--ornament-tone), rgba(235, 242, 236, 0) 70%);
  }
  .card__figure {
    position: absolute;
    left: 905px;
    top: 120px;
    width: 110px;
    height: 405px;
    border-radius: 50px;
    background: linear-gradient(180deg, #ffffff, var(--figure-tone));
    opacity: 0.85;
  }
  .card__tagline,
  .card__role,
  .card__phone {
    position: absolute;
    font-family: "Open Sans", "Helvetica Neue", Arial, sans-serif;
    font-weight: 400;
    white-space: nowrap;
    line-height: 1;
  }
  .card__tagline {
    left: 45px;
    top: 385px;
    font-size: 45px;
    color: var(--text-light);
    text-shadow: 1px 2px 3px rgba(0, 0, 0, 0.3);
  }
  .card__role {
    left: 196px;
    top: 455px;
    font-size: 45px;
    color: var(--text-accent);
    text-shadow: 1px 2px 3px rgba(0, 0, 0, 0.3);
  }
  .card__phone {
    left: 412px;
    top: 578px;
    font-size: 47px;
    color: var(--phone-ink);
  }
</style>
</head>
<body>
  <main class="canvas">
    <section class="card">
      <div class="card__field"></div>
      <div class="card__ornament" role="img" aria-label="Faint flowing floral swirl ornament"></div>
      <h1 class="card__title">WEXMOOR TAI CHI FOR FITNESS</h1>
      <div class="card__figure" role="img" aria-label="White silhouette of a person in a one-legged tree pose with arms raised"></div>
      <p class="card__tagline">Health &amp; Relaxation Branna Holt</p>
      <p class="card__role">Certificated Leader</p>
      <div class="card__band"></div>
      <p class="card__phone">Ph :&nbsp; 4091 5528</p>
    </section>
  </main>
</body>
</html>
```